Business Card Design

We are a full service general contractor that specializes in emergency services and insurance restoration/repair. Most of our work relates to water damage, fire dame, smoke, wind and hail, storm damage, etc. Pretty much anything you would call your insurance company for.

On one side of card the logo is VERY easy with the possibility of some modifications once I get a preview. I had a logo designed years ago and its on all my vehicles so I want to stick with my branding at this point and time.

Its a 2 sided card-for one side I would like the following:
* See logo (its attached)
* I would like this logo as large/big/bold as possible-essentially it should fill up the entire side of the card (barring it not looking proportionally correct of course)
* I think the background should be white behind it-or possibly red (with colors inverted so that they don't get lost in the red background)
* I'm attaching a photo of one of our work vans to go off of-you will notice that the .com wraps up the side of the logo-this .com portion needs to added on as the logo is only the kestrel restoration logo

The other side of the card I'm thinking should be:
* My biggest struggle is formatting-in other words-I don't know how to lay out all that info without the card looking jumbled/messy
* all our logos, vehicles, marketing media, etc. is based on or at least inspired by a clean look
* a smaller version of logo (without the .com) should be located somewhere on this side of card-I've seen some cards where its centered and others where its offset-I'm not sure which is better
* I could conceivably leave off PO BOX if its too much info and something needs deleted

Business

The logo will display company name-other pertinent info:
Phone: 704 555 0182
Mobile: 704 555 0147
Fax: 704 555 0163
email: kestrelrestoration@mailnest-example.com
Address: 2958 Willow Rd.
Brookvale, NC
PO BOX 60357 27999

```html
<!DOCTYPE html>
<html lang="en">
<head>
<meta charset="utf-8">
<title>Kestrel Restoration – Business Card</title>
<link href="https://fonts.googleapis.com/css2?family=Archivo+Black&family=Open+Sans:wght@400;600&display=swap" rel="stylesheet">
<style>
  :root {
    --stage: #000000;
    --paper: #ffffff;
    --ink: #1e1e1e;
    --charcoal: #2f353a;
    --brand-red: #c8141c;
    --red-top: #861a1f;
    --red-bottom: #b8060b;
  }
  html, body {
    margin: 0;
    padding: 0;
    width: 1200px;
    height: 900px;
    overflow: hidden;
    background: var(--stage);
  }
  .canvas {
    position: relative;
    width: 1200px;
    height: 900px;
  }
  .card {
    position: absolute;
    top: 275px;
    width: 477px;
    height: 293px;
    overflow: hidden;
  }
  .card--front {
    left: 116px;
    background: var(--paper);
    border-radius: 0 48px 0 48px;
  }
  .card--back {
    left: 622px;
    top: 276px;
    height: 292px;
    background: linear-gradient(180deg, var(--red-top) 0%, #9d0f15 55%, var(--red-bottom) 100%);
    border-radius: 48px 0 48px 0;
  }
  .wordmark {
    position: absolute;
    display: flex;
    align-items: center;
    gap: 10px;
    font-family: "Archivo Black", "Arial Black", sans-serif;
    line-height: 0.95;
  }
  .wordmark__square {
    width: 34px;
    height: 34px;
    flex: none;
  }
  .wordmark__name {
    display: block;
    font-size: 44px;
    letter-spacing: 0.5px;
  }
  .wordmark__sub {
    display: block;
    font-size: 21px;
    letter-spacing: 1px;
    margin-top: 4px;
  }
  .card--front .wordmark {
    left: 56px;
    top: 46px;
    color: var(--charcoal);
  }
  .card--front .wordmark__square { background: var(--brand-red); }
  .card--back .wordmark {
    left: 180px;
    top: 180px;
    color: var(--paper);
  }
  .card--back .wordmark__square { background: var(--paper); }
  .card--back .wordmark__name { font-size: 40px; }
  .card--back .wordmark__sub { font-size: 19px; }

  .contact {
    position: absolute;
    right: 28px;
    top: 158px;
    margin: 0;
    padding: 0;
    list-style: none;
    font-family: "Open Sans", Arial, sans-serif;
    font-size: 12.5px;
    color: var(--ink);
    text-align: right;
  }
  .contact__item {
    display: flex;
    justify-content: flex-end;
    align-items: center;
    gap: 7px;
    height: 20px;
  }
  .contact__icon {
    width: 10px;
    height: 10px;
    fill: var(--brand-red);
    flex: none;
  }
  .address {
    position: absolute;
    right: 28px;
    top: 244px;
    margin: 0;
    font-family: "Open Sans", Arial, sans-serif;
    font-size: 12.5px;
    color: var(--ink);
    font-style: normal;
    white-space: nowrap;
  }
</style>
</head>
<body>
<main class="canvas">
  <section class="card card--front">
    <div class="wordmark">
      <span class="wordmark__square"></span>
      <span>
        <span class="wordmark__name">KESTREL</span>
        <span class="wordmark__sub">RESTORATION</span>
      </span>
    </div>
    <ul class="contact">
      <li class="contact__item">704 555 0182
        <svg class="contact__icon" viewBox="0 0 10 10" aria-hidden="true"><path d="M2 0.5 L3.6 2.6 L2.7 3.6 Q3.8 5.9 6.3 7.3 L7.4 6.4 L9.5 8 L8.3 9.5 Q3.5 8.6 0.5 1.7 Z"/></svg>
      </li>
      <li class="contact__item">704 555 0147
        <svg class="contact__icon" viewBox="0 0 10 10" aria-hidden="true"><path d="M2.5 0 H7.5 V10 H2.5 Z M3.4 1.2 V7.8 H6.6 V1.2 Z M4.5 8.4 H5.5 V9.2 H4.5 Z"/></svg>
      </li>
      <li class="contact__item">704 555 0163
        <svg class="contact__icon" viewBox="0 0 10 10" aria-hidden="true"><path d="M2.5 0.5 H7.5 V3.5 H9.5 V9.5 H0.5 V3.5 H2.5 Z M3.3 1.3 V3.5 H6.7 V1.3 Z M2 5 V6 H3 V5 Z M4.5 5 V6 H5.5 V5 Z M7 5 V6 H8 V5 Z M2 7 V8 H3 V7 Z M4.5 7 V8 H5.5 V7 Z M7 7 V8 H8 V7 Z"/></svg>
      </li>
      <li class="contact__item">kestrelrestoration@mailnest-example.com
        <svg class="contact__icon" viewBox="0 0 10 10" aria-hidden="true"><path d="M0.5 2 H9.5 V8.5 H0.5 Z M1.3 2.6 L5 5.5 L8.7 2.6 Z" fill-rule="evenodd"/></svg>
      </li>
    </ul>
    <address class="address">2958 Willow Rd. Brookvale, NC PO BOX 60357 27999</address>
  </section>

  <section class="card card--back">
    <div class="wordmark">
      <span class="wordmark__square"></span>
      <span>
        <span class="wordmark__name">KESTREL</span>
        <span class="wordmark__sub">RESTORATION</span>
      </span>
    </div>
  </section>
</main>
</body>
</html>
```